Labels for my sauce bottles

I have designed the label- a few change suggestions are welcome<br/>but I basically need what is on the uploaded images- made high quality<br/>I don't have the programs to ensure it prints correctly and doesn't blur.<br/>I also have more labels to do- name, barcode and Nutritional Panel change- design/ concept stay the same<br/>dimensions are 190mm (long) x 75mm (High)

Font styles to use
Decorative
Script

Colors
ffc214

```html
<!DOCTYPE html>
<html lang="en">
<head>
<meta charset="utf-8">
<title>Ember Grove – Plump Pumpkin sauce labels</title>
<link rel="stylesheet" href="https://fonts.googleapis.com/css2?family=Kaushan+Script&family=Roboto:wght@400;700;900&family=Roboto+Condensed:wght@300&display=swap">
<style>
  :root {
    --gold: #ffc214;
    --ink: #ffffff;
    --board: #262626;
    --board-dark: #1b1b1b;
    --board-light: #333333;
    --rule: #e9e9e9;
    --panel-grey: #bdbdbd;
    --panel-line: #6a6a6a;
    --chilli-red: rgba(200, 20, 28, 0.55);
    --chilli-dark: rgba(60, 14, 20, 0.45);
  }
  * { box-sizing: border-box; margin: 0; padding: 0; }
  html, body { width: 969px; height: 1200px; overflow: hidden; background: #ffffff; }
  .sheet { position: relative; width: 969px; height: 1200px; }

  .label {
    position: absolute; left: 61px; width: 848px; height: 335px; overflow: hidden;
    color: var(--ink); font-family: "Roboto", Arial, sans-serif;
    background: radial-gradient(ellipse at 55% 45%, var(--board-light) 0%, var(--board) 55%, var(--board-dark) 100%);
  }
  .label--one { top: 61px; }
  .label--two { top: 432px; background: radial-gradient(ellipse at 45% 55%, #303030 0%, #242424 55%, #191919 100%); }
  .label--three { top: 805px; background: radial-gradient(ellipse at 60% 40%, #383838 0%, #2a2a2a 55%, #1e1e1e 100%); }

  .frame { position: absolute; inset: 0; width: 848px; height: 335px; }

  /* left column */
  .info { position: absolute; left: 8px; top: 20px; width: 202px; text-align: center; }
  .info__title { color: var(--gold); font-weight: 700; font-size: 16px; line-height: 20px; }
  .info__ingredients { font-weight: 700; font-size: 10.6px; line-height: 12px; margin-top: 4px; }
  .info__note { color: var(--gold); font-weight: 700; font-size: 11.5px; line-height: 14px; margin-top: 8px; }
  .info__storage { font-weight: 700; font-size: 11.8px; line-height: 14px; margin-top: 1px; }

  .nutrition {
    position: absolute; left: 38px; top: 127px; width: 141px; height: 172px;
    border: 1.5px solid var(--panel-grey); padding: 2px 4px;
  }
  .nutrition__title { font-weight: 900; font-size: 17.5px; color: #e4e4e4; line-height: 19px; white-space: nowrap; letter-spacing: -0.2px; }
  .nutrition__serving { font-size: 6.2px; line-height: 8.5px; margin-top: 2px; }
  .nutrition__bar { height: 4px; background: var(--panel-grey); margin: 3px 0 2px; }
  .nutrition table { width: 100%; border-collapse: collapse; font-size: 6.2px; table-layout: fixed; }
  .nutrition col.col-name { width: 50px; }
  .nutrition th { font-weight: 400; text-align: left; line-height: 8px; padding: 1px 0 2px; vertical-align: top; border-bottom: 4px solid var(--panel-grey); }
  .nutrition td { line-height: 11.9px; border-bottom: 0.5px solid var(--panel-line); white-space: nowrap; }
  .nutrition td:nth-child(2), .nutrition td:nth-child(3) { text-align: center; }
  .nutrition .is-main { font-weight: 700; }
  .nutrition .is-sub { padding-left: 13px; }
  .nutrition tr:last-child td { border-bottom: none; }
  .footnote { position: absolute; left: 35px; top: 305px; font-size: 7.5px; white-space: nowrap; }

  /* centre */
  .chilli-art {
    position: absolute; left: 420px; top: 28px; width: 110px; height: 262px;
    background: radial-gradient(ellipse 50% 50% at 50% 45%, var(--chilli-red) 0%, var(--chilli-dark) 60%, rgba(0,0,0,0) 100%);
  }
  .tagline { position: absolute; font-family: "Kaushan Script", cursive; font-size: 19px; line-height: 1; color: var(--ink); white-space: nowrap; }
  .tagline--left { left: 370px; top: 33px; transform: rotate(-4deg); }
  .tagline--right { left: 492px; top: 45px; transform: rotate(-3deg); }

  .brand { position: absolute; font-family: "Kaushan Script", cursive; color: var(--ink); white-space: nowrap; line-height: 1; font-weight: 400; }
  .brand--first { left: 305px; top: 112px; font-size: 62px; }
  .brand--second { left: 468px; top: 132px; font-size: 74px; }
  .sprig { position: absolute; width: 36px; height: 38px; border-radius: 50%;
    background: radial-gradient(ellipse at center, rgba(230,230,230,.45) 0%, rgba(230,230,230,.15) 55%, rgba(0,0,0,0) 72%); }
  .sprig--left { left: 266px; top: 132px; }
  .sprig--right { left: 656px; top: 160px; }

  .flavour { position: absolute; left: 322px; width: 300px; top: 234px; text-align: center;
    font-family: "Kaushan Script", cursive; font-size: 38px; color: var(--gold); white-space: nowrap; line-height: 1; }
  .volume { position: absolute; left: 421px; width: 100px; top: 295px; text-align: center;
    font-family: "Roboto Condensed", Arial, sans-serif; font-weight: 300; font-size: 19px; line-height: 22px; }

  /* right column */
  .maker { position: absolute; left: 729px; top: 18px; width: 106px; text-align: center; color: var(--gold);
    font-weight: 700; font-size: 12.3px; line-height: 14px; }
  .social { position: absolute; left: 729px; top: 74px; width: 106px; display: flex; align-items: center; justify-content: center; gap: 4px;
    color: var(--gold); font-weight: 700; font-size: 10px; line-height: 12px; }
  .social__dot { width: 10px; height: 10px; border-radius: 50%; background: var(--gold); }
  .field-label { position: absolute; left: 743px; font-size: 11px; line-height: 13px; }
  .field-label--batch { top: 247px; }
  .field-label--best { top: 283px; }
  .field-box { position: absolute; left: 744px; width: 78px; height: 14px; background: #ffffff; }
  .field-box--batch { top: 261px; }
  .field-box--best { top: 297px; }
</style>
</head>
<body>
<main class="sheet">

  <section class="label label--one">
    <svg class="frame" viewBox="0 0 848 335" aria-hidden="true">
      <g stroke="#e9e9e9" fill="none">
        <line x1="30" y1="13" x2="72" y2="13" stroke-width="1" stroke-dasharray="1.5 1.5"/>
        <line x1="80" y1="10" x2="260" y2="8" stroke-width=".8"/>
        <line x1="330" y1="8" x2="700" y2="8" stroke-width=".8"/>
        <line x1="680" y1="13" x2="826" y2="13" stroke-width="1" stroke-dasharray="1.5 1.5"/>
        <line x1="10" y1="20" x2="10" y2="310" stroke-width="1"/>
        <line x1="838" y1="20" x2="838" y2="310" stroke-width="1"/>
        <line x1="15" y1="60" x2="15" y2="280" stroke-width="1" stroke-dasharray="1.5 1.5"/>
        <line x1="833" y1="60" x2="833" y2="280" stroke-width="1" stroke-dasharray="1.5 1.5"/>
        <line x1="24" y1="322" x2="68" y2="322" stroke-width="1" stroke-dasharray="1.5 1.5"/>
        <line x1="60" y1="327" x2="700" y2="327" stroke-width=".8"/>
        <line x1="740" y1="322" x2="822" y2="322" stroke-width="1" stroke-dasharray="1.5 1.5"/>
        <path d="M352 62 Q410 52 470 52" stroke-width="1.5"/>
        <path d="M486 76 Q560 68 622 62" stroke-width="1.5"/>
        <path d="M385 307 Q412 304 439 307" stroke-width="1.5"/>
        <path d="M503 307 Q530 304 556 307" stroke-width="1.5"/>
      </g>
    </svg>
    <div class="info">
      <h2 class="info__title">Ingredients:</h2>
      <p class="info__ingredients">Pumpkin, Coconut Cream, Vinegar,<br>Habaneros, Fatalii Medley,<br>Butter, Garlic, Peppercorns, Salt</p>
      <p class="info__note">No Artificial Additives</p>
      <p class="info__storage">Refrigerate after opening</p>
    </div>
    <div class="nutrition">
      <h3 class="nutrition__title">Nutrition Facts</h3>
      <p class="nutrition__serving">Serving per package: 16.60<br>Serving size: 15.00 ml</p>
      <div class="nutrition__bar"></div>
      <table>
        <colgroup><col class="col-name"><col><col></colgroup>
        <tr><th></th><th>Average<br>Quantity<br>per Serving</th><th>Average<br>Quantity<br>per 100 ml</th></tr>
        <tr><td class="is-main">Energy</td><td>79 kJ</td><td>529 kJ</td></tr>
        <tr><td class="is-main">Protein</td><td>0.5 g</td><td>3.4 g</td></tr>
        <tr><td class="is-main">Fat, total</td><td>1.3 g</td><td>8.6 g</td></tr>
        <tr><td class="is-sub">Saturated</td><td>1.0 g</td><td>6.9 g</td></tr>
        <tr><td class="is-main">Carbohydrate</td><td>1.4 g</td><td>9.7 g</td></tr>
        <tr><td class="is-sub">Sugars</td><td>1.0 g</td><td>6.4 g</td></tr>
        <tr><td class="is-main">Sodium</td><td>24 mg</td><td>162 mg</td></tr>
      </table>
    </div>
    <p class="footnote">*Based on the average adult daily intake</p>

    <div class="chilli-art" role="img" aria-label="Painted chilli illustration, red with green stem, dipped in dark chocolate"></div>
    <span class="tagline tagline--left">Small batch</span>
    <span class="tagline tagline--right">Craft sauce</span>
    <div class="sprig sprig--left" role="img" aria-label="Leaf sprig decoration"></div>
    <div class="sprig sprig--right" role="img" aria-label="Leaf sprig decoration"></div>
    <h1 class="brand brand--first">Ember</h1>
    <span class="brand brand--second">Grove</span>
    <p class="flavour">Plump Pumpkin</p>
    <p class="volume">250ml</p>

    <p class="maker">Produced and<br>Bottled on the<br>Saltbush Coast</p>
    <p class="social"><span class="social__dot"></span>@embergrove</p>
    <p class="field-label field-label--batch">Batch Number</p>
    <div class="field-box field-box--batch"></div>
    <p class="field-label field-label--best">Best Before</p>
    <div class="field-box field-box--best"></div>
  </section>

  <section class="label label--two">
    <svg class="frame" viewBox="0 0 848 335" aria-hidden="true">
      <g stroke="#e9e9e9" fill="none">
        <line x1="30" y1="13" x2="72" y2="13" stroke-width="1" stroke-dasharray="1.5 1.5"/>
        <line x1="80" y1="10" x2="260" y2="8" stroke-width=".8"/>
        <line x1="330" y1="8" x2="700" y2="8" stroke-width=".8"/>
        <line x1="680" y1="13" x2="826" y2="13" stroke-width="1" stroke-dasharray="1.5 1.5"/>
        <line x1="10" y1="20" x2="10" y2="310" stroke-width="1"/>
        <line x1="838" y1="20" x2="838" y2="310" stroke-width="1"/>
        <line x1="15" y1="60" x2="15" y2="280" stroke-width="1" stroke-dasharray="1.5 1.5"/>
        <line x1="833" y1="60" x2="833" y2="280" stroke-width="1" stroke-dasharray="1.5 1.5"/>
        <line x1="24" y1="322" x2="68" y2="322" stroke-width="1" stroke-dasharray="1.5 1.5"/>
        <line x1="60" y1="327" x2="700" y2="327" stroke-width=".8"/>
        <line x1="740" y1="322" x2="822" y2="322" stroke-width="1" stroke-dasharray="1.5 1.5"/>
        <path d="M352 62 Q410 52 470 52" stroke-width="1.5"/>
        <path d="M486 76 Q560 68 622 62" stroke-width="1.5"/>
        <path d="M385 307 Q412 304 439 307" stroke-width="1.5"/>
        <path d="M503 307 Q530 304 556 307" stroke-width="1.5"/>
      </g>
    </svg>
    <div class="info">
      <h2 class="info__title">Ingredients:</h2>
      <p class="info__ingredients">Pumpkin, Coconut Cream, Vinegar,<br>Habaneros, Fatalii Medley,<br>Butter, Garlic, Peppercorns, Salt</p>
      <p class="info__note">No Artificial Additives</p>
      <p class="info__storage">Refrigerate after opening</p>
    </div>
    <div class="nutrition">
      <h3 class="nutrition__title">Nutrition Facts</h3>
      <p class="nutrition__serving">Serving per package: 16.60<br>Serving size: 15.00 ml</p>
      <div class="nutrition__bar"></div>
      <table>
        <colgroup><col class="col-name"><col><col></colgroup>
        <tr><th></th><th>Average<br>Quantity<br>per Serving</th><th>Average<br>Quantity<br>per 100 ml</th></tr>
        <tr><td class="is-main">Energy</td><td>79 kJ</td><td>529 kJ</td></tr>
        <tr><td class="is-main">Protein</td><td>0.5 g</td><td>3.4 g</td></tr>
        <tr><td class="is-main">Fat, total</td><td>1.3 g</td><td>8.6 g</td></tr>
        <tr><td class="is-sub">Saturated</td><td>1.0 g</td><td>6.9 g</td></tr>
        <tr><td class="is-main">Carbohydrate</td><td>1.4 g</td><td>9.7 g</td></tr>
        <tr><td class="is-sub">Sugars</td><td>1.0 g</td><td>6.4 g</td></tr>
        <tr><td class="is-main">Sodium</td><td>24 mg</td><td>162 mg</td></tr>
      </table>
    </div>
    <p class="footnote">*Based on the average adult daily intake</p>

    <div class="chilli-art" role="img" aria-label="Painted chilli illustration, red with green stem, dipped in dark chocolate"></div>
    <span class="tagline tagline--left">Small batch</span>
    <span class="tagline tagline--right">Craft sauce</span>
    <div class="sprig sprig--left" role="img" aria-label="Leaf sprig decoration"></div>
    <div class="sprig sprig--right" role="img" aria-label="Leaf sprig decoration"></div>
    <p class="brand brand--first">Ember</p>
    <span class="brand brand--second">Grove</span>
    <p class="flavour">Plump Pumpkin</p>
    <p class="volume">250ml</p>

    <p class="maker">Produced and<br>Bottled on the<br>Saltbush Coast</p>
    <p class="social"><span class="social__dot"></span>@embergrove</p>
    <p class="field-label field-label--batch">Batch Number</p>
    <div class="field-box field-box--batch"></div>
    <p class="field-label field-label--best">Best Before</p>
    <div class="field-box field-box--best"></div>
  </section>

  <section class="label label--three">
    <svg class="frame" viewBox="0 0 848 335" aria-hidden="true">
      <g stroke="#e9e9e9" fill="none">
        <line x1="30" y1="13" x2="72" y2="13" stroke-width="1" stroke-dasharray="1.5 1.5"/>
        <line x1="80" y1="10" x2="260" y2="8" stroke-width=".8"/>
        <line x1="330" y1="8" x2="700" y2="8" stroke-width=".8"/>
        <line x1="680" y1="13" x2="826" y2="13" stroke-width="1" stroke-dasharray="1.5 1.5"/>
        <line x1="10" y1="20" x2="10" y2="310" stroke-width="1"/>
        <line x1="838" y1="20" x2="838" y2="310" stroke-width="1"/>
        <line x1="15" y1="60" x2="15" y2="280" stroke-width="1" stroke-dasharray="1.5 1.5"/>
        <line x1="833" y1="60" x2="833" y2="280" stroke-width="1" stroke-dasharray="1.5 1.5"/>
        <line x1="24" y1="322" x2="68" y2="322" stroke-width="1" stroke-dasharray="1.5 1.5"/>
        <line x1="60" y1="327" x2="700" y2="327" stroke-width=".8"/>
        <line x1="740" y1="322" x2="822" y2="322" stroke-width="1" stroke-dasharray="1.5 1.5"/>
        <path d="M352 62 Q410 52 470 52" stroke-width="1.5"/>
        <path d="M486 76 Q560 68 622 62" stroke-width="1.5"/>
        <path d="M385 307 Q412 304 439 307" stroke-width="1.5"/>
        <path d="M503 307 Q530 304 556 307" stroke-width="1.5"/>
      </g>
    </svg>
    <div class="info">
      <h2 class="info__title">Ingredients:</h2>
      <p class="info__ingredients">Pumpkin, Coconut Cream, Vinegar,<br>Habaneros, Fatalii Medley,<br>Butter, Garlic, Peppercorns, Salt</p>
      <p class="info__note">No Artificial Additives</p>
      <p class="info__storage">Refrigerate after opening</p>
    </div>
    <div class="nutrition">
      <h3 class="nutrition__title">Nutrition Facts</h3>
      <p class="nutrition__serving">Serving per package: 16.60<br>Serving size: 15.00 ml</p>
      <div class="nutrition__bar"></div>
      <table>
        <colgroup><col class="col-name"><col><col></colgroup>
        <tr><th></th><th>Average<br>Quantity<br>per Serving</th><th>Average<br>Quantity<br>per 100 ml</th></tr>
        <tr><td class="is-main">Energy</td><td>79 kJ</td><td>529 kJ</td></tr>
        <tr><td class="is-main">Protein</td><td>0.5 g</td><td>3.4 g</td></tr>
        <tr><td class="is-main">Fat, total</td><td>1.3 g</td><td>8.6 g</td></tr>
        <tr><td class="is-sub">Saturated</td><td>1.0 g</td><td>6.9 g</td></tr>
        <tr><td class="is-main">Carbohydrate</td><td>1.4 g</td><td>9.7 g</td></tr>
        <tr><td class="is-sub">Sugars</td><td>1.0 g</td><td>6.4 g</td></tr>
        <tr><td class="is-main">Sodium</td><td>24 mg</td><td>162 mg</td></tr>
      </table>
    </div>
    <p class="footnote">*Based on the average adult daily intake</p>

    <div class="chilli-art" role="img" aria-label="Painted chilli illustration, red with green stem, dipped in dark chocolate"></div>
    <span class="tagline tagline--left">Small batch</span>
    <span class="tagline tagline--right">Craft sauce</span>
    <div class="sprig sprig--left" role="img" aria-label="Leaf sprig decoration"></div>
    <div class="sprig sprig--right" role="img" aria-label="Leaf sprig decoration"></div>
    <p class="brand brand--first">Ember</p>
    <span class="brand brand--second">Grove</span>
    <p class="flavour">Plump Pumpkin</p>
    <p class="volume">250ml</p>

    <p class="maker">Produced and<br>Bottled on the<br>Saltbush Coast</p>
    <p class="social"><span class="social__dot"></span>@embergrove</p>
    <p class="field-label field-label--batch">Batch Number</p>
    <div class="field-box field-box--batch"></div>
    <p class="field-label field-label--best">Best Before</p>
    <div class="field-box field-box--best"></div>
  </section>

</main>
</body>
</html>
```